Most captivating card ever!

Life Coach - Professional Adventurer - Entrepreneur
I need the worlds most amazing business card for my personal brand. This business card will mostly be used to give to prospective clients for life coaching and business coaching.
Be creative, be adventurous. It needs to stand out. Make people say.. I need this guy!
My background is as an entrepreneur and professional adventurer undertaking extreme expeditions. I am now moving into life coaching.
No specific design ideas, so you have full creativity. Show me your best.
Industry/Entity Type
Life Coaching
Contact Information for Business Card
Dan Pellow
itsdanp.com.au
0468215903
Colors
Designer to choose colors to be used in the design.
Look and feel

```html
<!DOCTYPE html>
<html lang="en">
<head>
<meta charset="utf-8">
<title>Dan Pellow – Business Card</title>
<link href="https://fonts.googleapis.com/css2?family=Oswald:wght@600&family=Open+Sans:wght@400;700&display=swap" rel="stylesheet">
<style>
  :root {
    --backdrop: #eceeea;
    --card: #ffffff;
    --green: #6db33f;
    --green-deep: #63a838;
    --orange-text: #e8a04a;
    --white: #ffffff;
  }
  html, body {
    margin: 0;
    padding: 0;
    width: 1200px;
    height: 802px;
    overflow: hidden;
    background: var(--backdrop);
  }
  .canvas {
    position: relative;
    width: 1200px;
    height: 802px;
  }
  .card {
    position: absolute;
    left: 150px;
    top: 151px;
    width: 900px;
    height: 500px;
    background: var(--card);
    overflow: hidden;
    box-shadow: 0 6px 24px rgba(0,0,0,0.12);
  }
  .card__band {
    position: absolute;
    left: 0;
    right: 0;
    top: 345px;
    bottom: 0;
    background: linear-gradient(180deg, var(--green) 0%, var(--green-deep) 100%);
  }
  .identity {
    position: absolute;
    left: 0;
    width: 840px;
    top: 150px;
    text-align: center;
  }
  .identity__name {
    margin: 0;
    font-family: "Oswald", sans-serif;
    font-weight: 600;
    font-size: 48px;
    line-height: 1.1;
    color: var(--green);
    letter-spacing: 0.5px;
  }
  .identity__roles {
    margin: 10px 0 0;
    font-family: "Open Sans", sans-serif;
    font-weight: 700;
    font-size: 15px;
    color: var(--orange-text);
    letter-spacing: 0.6px;
  }
  .contact {
    position: absolute;
    left: 636px;
    top: 386px;
    margin: 0;
    padding: 0;
    list-style: none;
    font-family: "Open Sans", sans-serif;
    font-size: 19px;
    color: var(--white);
  }
  .contact__item {
    display: flex;
    align-items: center;
    gap: 14px;
    height: 40px;
  }
  .contact__icon {
    width: 20px;
    height: 20px;
    fill: var(--white);
    flex: none;
  }
</style>
</head>
<body>
<div class="canvas">
  <div class="card">
    <div class="card__band" role="img" aria-label="Green band with orange swoosh accents across the lower part of the card"></div>

    <div class="identity">
      <h1 class="identity__name">Dan Pellow</h1>
      <p class="identity__roles">Life Coach - Professional Adventurer - Entrepreneur</p>
    </div>

    <ul class="contact">
      <li class="contact__item">
        <svg class="contact__icon" viewBox="0 0 24 24" aria-hidden="true">
          <path d="M6.6 10.8a15.1 15.1 0 0 0 6.6 6.6l2.2-2.2a1 1 0 0 1 1-.25 11.4 11.4 0 0 0 3.6.57 1 1 0 0 1 1 1V20a1 1 0 0 1-1 1A17 17 0 0 1 3 4a1 1 0 0 1 1-1h3.5a1 1 0 0 1 1 1c0 1.25.2 2.45.57 3.57a1 1 0 0 1-.25 1z"/>
        </svg>
        <span>0468215903</span>
      </li>
      <li class="contact__item">
        <svg class="contact__icon" viewBox="0 0 24 24" aria-hidden="true">
          <path d="M12 2a10 10 0 1 0 5 18.66l-1-1.73A8 8 0 1 1 20 12v1.5a1.5 1.5 0 0 1-3 0V12a5 5 0 1 0-1.46 3.53A3.5 3.5 0 0 0 22 13.5V12A10 10 0 0 0 12 2zm0 13a3 3 0 1 1 0-6 3 3 0 0 1 0 6z"/>
        </svg>
        <span>itsdanp.com.au</span>
      </li>
    </ul>
  </div>
</div>
</body>
</html>
```